Wedding Startup Full Website Design

We've just completed our online platform and need to create a website that represents our brand and vision, and clearly communicates our features and value proposition to potential users. There are a minimum of 4 pages that need to be designed. One geared toward wedding professionals (venues/vendors/coordinators), another toward engaged couples, one showcasing features, and an 'About Us' page.

The designer will creative freedom to create a unique UI/UX as long as it represents our brand and is relevant to our target audience/market. The ideal candidate will be able to assume the mindset of someone working in the wedding industry and/or an engaged couple. Ability to create illustrations is a plus.

Copy will be provided as needed. We will reimburse for stock images (pending approval before purchasing), but sourcing the stock images will be the responsibility of the designer.

Our current website: https://www.marquiso.com
Updates

Still waiting for a design that stands out from the rest and aligns with the creative brief.

Target Market(s)

Wedding Professionals and Engaged Couples

Industry/Entity Type

Wedding

Number of Pages Required

4 page

Font styles to use
Sans Serif

Colors
ffffff
fbd4d5
f59195
33a6d7
cadf82
86cfc6

Requirements
Must have
• Common sense stuff like having a unified brand that accurately represents our platform, speaks to our target market, and clearly articulates our vision
Nice to have
• Illustrations
Should not have
• Overly cheesy or childish. We want to be professional but still embrace the wedding culture.

```html
<!DOCTYPE html>
<html lang="en">
<head>
<meta charset="utf-8">
<title>Marquiso — Wedding Planning Platform</title>
<link href="https://fonts.googleapis.com/css2?family=Poppins:wght@300;400;500;600&display=swap" rel="stylesheet">
<style>
:root{
  --white:#ffffff;
  --blush:#fbd4d5;
  --rose:#f59195;
  --rose-deep:#ef7f86;
  --sky:#33a6d7;
  --ink:#333333;
  --grey:#666666;
  --card:#f4f4f4;
  --petal:#fdf0f0;
  --night:#141414;
}
*{box-sizing:border-box;margin:0;padding:0}
html,body{width:1200px;height:2922px;overflow:hidden;background:var(--white)}
body{position:relative;font-family:'Poppins',sans-serif;color:var(--ink)}
.abs{position:absolute}

/* header */
.top-rule{left:0;top:0;width:1200px;height:5px;background:var(--rose)}
.site-header{left:0;top:5px;width:1200px;height:96px;background:var(--white)}
.brand{font-family:'Poppins',sans-serif;font-weight:400;color:var(--sky);display:flex;align-items:center;gap:10px}
.brand-dot{width:14px;height:14px;border-radius:50%;background:var(--rose)}
.site-header .brand{left:86px;top:22px;font-size:40px}
.nav{top:38px;font-size:15px;color:var(--ink)}
.nav.active{color:var(--sky)}
.nav.active::after{content:"";position:absolute;left:0;right:0;top:26px;height:2px;background:var(--rose)}
.nav-divider{left:943px;top:38px;width:1px;height:18px;background:#ccc}
.phone{left:984px;top:38px;font-size:15px;display:flex;align-items:center;gap:10px}

/* hero */
.hero{left:0;top:101px;width:1200px;height:489px;background:linear-gradient(180deg,#4a2f9a 0%,#7b5ac9 35%,#b59adb 60%,#8c6aa8 100%)}
.hero-frame{left:191px;top:302px;width:818px;height:88px;border:2px solid var(--rose)}
.hero-title{left:0;top:268px;width:1200px;text-align:center;font-size:48px;font-weight:500;color:var(--white);letter-spacing:1px}
.hero-sub{left:0;top:331px;width:1200px;text-align:center;font-size:20px;font-weight:500;color:var(--white);letter-spacing:5px}
.btn{display:flex;align-items:center;justify-content:center;background:var(--sky);color:var(--white);font-size:15px;letter-spacing:2px;font-weight:400}
.hero .btn{left:495px;top:273px;width:210px;height:33px}

/* feature cards */
.card{top:655px;width:326px;height:128px;background:var(--card);box-shadow:0 3px 6px rgba(0,0,0,.12)}
.card svg{position:absolute;left:16px;top:28px}
.card h3{position:absolute;left:88px;top:20px;font-size:21px;font-weight:400;color:var(--rose)}
.card p{position:absolute;left:88px;top:52px;width:222px;font-size:13px;line-height:19px;color:var(--ink)}

/* professionals */
.pros{left:0;top:843px;width:1200px;height:602px;background:var(--petal)}
.section-title{left:0;width:1200px;text-align:center;font-size:32px;font-weight:400;color:var(--sky)}
.title-rule{left:536px;width:128px;height:2px;background:var(--rose)}
.title-rule::after{content:"";position:absolute;left:24px;top:6px;width:80px;height:1px;background:var(--rose)}
.photo-circle{width:242px;height:242px;border-radius:50%;border:6px solid var(--white);box-shadow:0 2px 6px rgba(0,0,0,.12)}
.pro-name{width:320px;text-align:center;font-size:21px;color:var(--rose)}
.pro-text{width:260px;text-align:center;font-size:13px;line-height:19px;color:var(--grey)}

/* couples */
.cake{left:493px;top:1578px;width:214px;height:340px;border-radius:40px 40px 20px 20px;background:linear-gradient(180deg,#f7d7dc 0%,#f08aa0 55%,#d9607e 100%)}
.couple-head{font-size:21px;color:var(--rose)}
.couple-text{width:322px;font-size:13px;line-height:20px;color:var(--grey)}
.right-col{text-align:right}

/* why choose */
.why{left:0;top:2041px;width:1200px;height:542px;background:linear-gradient(120deg,#f29ba2 0%,#f08d94 45%,#e8a0a6 75%,#d98b88 100%)}
.why-title{left:86px;top:2094px;font-size:32px;font-weight:400;color:var(--white)}
.why-rule{left:86px;top:2148px;width:128px;height:2px;background:var(--white)}
.why-icon{left:103px}
.why-head{left:175px;font-size:21px;color:var(--white)}
.why-text{left:175px;font-size:13px;color:rgba(255,255,255,.85)}

/* footer */
.footer{left:0;top:2583px;width:1200px;height:339px;background:var(--night)}
.foot-head{font-size:16px;color:var(--white);letter-spacing:1px;font-weight:500}
.field{left:86px;width:327px;border:1px solid #555;font-size:13px;color:#aaa;padding:7px 12px}
.foot-link{left:592px;font-size:13px;color:#ccc}
.social{top:2792px;width:32px;height:32px;border-radius:50%;background:var(--white)}
.copy{left:927px;font-size:13px;color:#ccc;line-height:21px}
</style>
</head>
<body>

<div class="abs top-rule"></div>
<header class="abs site-header">
  <div class="abs brand"><span class="brand-dot"></span>Marquiso</div>
</header>
<a class="abs nav active" style="left:403px">Home</a>
<a class="abs nav" style="left:475px">About Us</a>
<a class="abs nav" style="left:569px">Wedding Professionals</a>
<a class="abs nav" style="left:773px">Engaged Couples</a>
<div class="abs nav-divider"></div>
<div class="abs phone">
  <svg width="14" height="14" viewBox="0 0 24 24"><path d="M6.6 10.8a15 15 0 0 0 6.6 6.6l2.2-2.2a1 1 0 0 1 1-.25 11.4 11.4 0 0 0 3.6.6 1 1 0 0 1 1 1V20a1 1 0 0 1-1 1A17 17 0 0 1 3 4a1 1 0 0 1 1-1h3.5a1 1 0 0 1 1 1c0 1.25.2 2.45.6 3.6a1 1 0 0 1-.25 1z" fill="var(--sky)"/></svg>
  0198 765 4320
</div>

<section class="abs hero" role="img" aria-label="Wedding reception hall with tall tiered cake, white flower arrangements and violet drapery">
  <a class="abs btn">GET STARTED</a>
</section>
<div class="abs hero-frame"></div>
<h1 class="abs hero-title">WELCOME TO MARQUISO</h1>
<p class="abs hero-sub">WE CHANGING THE WEDDING PLANNING PROCESS!</p>

<!-- feature cards -->
<div class="abs card" style="left:86px">
  <svg width="58" height="60" viewBox="0 0 58 60" fill="none" stroke="var(--rose)" stroke-width="2"><circle cx="29" cy="18" r="10"/><path d="M25 28v6h8v-6M29 2v3M14 8l2 2M44 8l-2 2M10 18h3M45 18h3"/><path d="M4 44h14l12 4h14l10-6M4 52h16l14 4 20-10"/></svg>
  <h3>Inspire</h3>
  <p>Inspire innovation and bringing dream weddings to life.</p>
</div>
<div class="abs card" style="left:438px">
  <svg width="58" height="60" viewBox="0 0 58 60" fill="none" stroke="var(--rose)" stroke-width="2"><path d="M8 14l12-4 6 16a6 6 0 0 1-11 4zM14 32l4 14M10 48l14-5"/><path d="M50 14l-12-4-6 16a6 6 0 0 0 11 4zM44 32l-4 14M48 48l-14-5"/><path d="M26 4l3 4M32 4l-3 4"/></svg>
  <h3>Enjoy</h3>
  <p>For wedding professions and couples to enjoy the wedding planning experience.</p>
</div>
<div class="abs card" style="left:789px">
  <svg width="58" height="60" viewBox="0 0 58 60" fill="none" stroke="var(--rose)" stroke-width="2"><path d="M29 58V10M29 22c-10 0-14-8-14-8s10-2 14 8M29 34c10 0 14-8 14-8s-10-2-14 8M29 46c-10 0-14-8-14-8s10-2 14 8M29 10c0-6 4-8 4-8"/><path d="M16 58h26"/></svg>
  <h3>GROW</h3>
  <p>Foster growth for our partners and within the wedding industry.</p>
</div>

<!-- wedding professionals -->
<section class="abs pros" role="img" aria-label="Soft pink background with faint floral pattern"></section>
<h2 class="abs section-title" style="top:895px">Wedding Professionals</h2>
<div class="abs title-rule" style="top:950px"></div>

<div class="abs photo-circle" style="left:126px;top:983px;background:linear-gradient(180deg,#f4f1e8 0%,#2b2a26 40%,#9a3f6a 65%,#6a9a3a 100%)" role="img" aria-label="Tented wedding venue with rows of chairs dressed in purple sashes"></div>
<div class="abs photo-circle" style="left:479px;top:983px;background:linear-gradient(180deg,#9b8d7a 0%,#c9b79b 45%,#e06a78 100%)" role="img" aria-label="Wedding vendor exhibition hall with booths"></div>
<div class="abs photo-circle" style="left:830px;top:983px;background:linear-gradient(135deg,#e7e3e3 0%,#b07a5a 40%,#f1e9e6 100%)" role="img" aria-label="Coordinator helping a bride prepare"></div>

<h3 class="abs pro-name" style="left:87px;top:1235px">Professional Venues</h3>
<h3 class="abs pro-name" style="left:440px;top:1235px">Professional Vendors</h3>
<h3 class="abs pro-name" style="left:791px;top:1235px">Coordinators</h3>
<p class="abs pro-text" style="left:117px;top:1268px">Lorem Ipsum is simply dummy text of the printing and typesetting industry.</p>
<p class="abs pro-text" style="left:470px;top:1268px">It is a long established fact that a reader will be distracted by the readable content</p>
<p class="abs pro-text" style="left:821px;top:1268px">Contrary to popular belief, Lorem Ipsum is not industry simply random text.</p>
<a class="abs btn" style="left:526px;top:1348px;width:148px;height:37px;letter-spacing:1px">LEARN MORE</a>

<!-- engaged couples -->
<h2 class="abs section-title" style="top:1499px">Engaged Couples</h2>
<div class="abs title-rule" style="top:1554px"></div>
<div class="abs cake" role="img" aria-label="Tiered pink wedding cake with sugar roses and a couple topper"></div>

<h3 class="abs couple-head right-col" style="left:91px;width:322px;top:1609px">Vision</h3>
<p class="abs couple-text right-col" style="left:91px;top:1641px">Every couple has a vision of what their special day will be like. Marquiso provides the tools to clearly and concisely communicate that to others.</p>
<h3 class="abs couple-head right-col" style="left:91px;width:322px;top:1749px">Organize</h3>
<p class="abs couple-text right-col" style="left:91px;top:1781px">We know every detail is important when it comes to your special day. That's why we make it easy to stay organized so nothing is left out or forgotten.</p>

<h3 class="abs couple-head" style="left:789px;top:1609px">Create</h3>
<p class="abs couple-text" style="left:789px;top:1641px">Taking your vision and communicating it to others can be difficult. With Marquiso, we provide tools to help make the process better, ensuring your wedding day isn't just a dream.</p>
<h3 class="abs couple-head" style="left:789px;top:1749px">Monitor</h3>
<p class="abs couple-text" style="left:789px;top:1781px">It's important to stay on track when planning. Within Marquiso you know exactly where you are in the process and what is needed to keep everything running smoothly.</p>
<a class="abs btn" style="left:526px;top:1944px;width:148px;height:37px;letter-spacing:1px">LEARN MORE</a>

<!-- why choose -->
<section class="abs why" role="img" aria-label="Blurred pink rose centerpiece on a reception table"></section>
<h2 class="abs why-title">Why Choose Marquiso</h2>
<div class="abs why-rule"></div>

<svg class="abs why-icon" style="top:2180px" width="46" height="46" viewBox="0 0 46 46" fill="none" stroke="#fff" stroke-width="3"><circle cx="23" cy="23" r="19"/><path d="M23 11v12h9"/></svg>
<h3 class="abs why-head" style="top:2174px">Saves Everyone Time</h3>
<p class="abs why-text" style="top:2205px">Marquiso streamlines certain processes allowing you to spend more time on the things you want to or just relax!</p>

<svg class="abs why-icon" style="top:2256px" width="46" height="46" viewBox="0 0 46 46" fill="none" stroke="#fff" stroke-width="2.5"><path d="M4 6h38v26H18l-9 8v-8H4z"/><path d="M11 15h24M11 23h18"/></svg>
<h3 class="abs why-head" style="top:2254px">Better Client Reviews</h3>
<p class="abs why-text" style="top:2285px">With Marquiso you can offer your clients an experience they will rave about, leading to better reviews and more clients.</p>

<svg class="abs why-icon" style="top:2330px" width="46" height="46" viewBox="0 0 46 46" fill="none" stroke="#fff" stroke-width="2.5"><rect x="3" y="5" width="32" height="24" rx="2"/><path d="M12 36h14M19 29v7"/><rect x="28" y="18" width="14" height="24" rx="2"/></svg>
<h3 class="abs why-head" style="top:2328px">Accessible on Any Device</h3>
<p class="abs why-text" style="top:2359px">Flexibility is key, which is why Marquiso's platform was built to be accessed on your phone, tablet or desktop.</p>

<svg class="abs why-icon" style="top:2408px" width="46" height="46" viewBox="0 0 46 46" fill="none" stroke="#fff" stroke-width="2.5"><rect x="8" y="5" width="30" height="38" rx="2"/><path d="M17 3h12v6H17zM14 18l3 3 5-5M25 19h8M14 30l3 3 5-5M25 31h8"/></svg>
<h3 class="abs why-head" style="top:2407px">Simplified Organization</h3>
<p class="abs why-text" style="top:2438px">Marquiso was built with organization in mind. All event details are in one place making executing an event easier.</p>

<svg class="abs why-icon" style="top:2480px" width="46" height="46" viewBox="0 0 46 46" fill="none" stroke="#fff" stroke-width="2.5"><rect x="4" y="10" width="38" height="24" rx="3"/><path d="M4 17h38M10 27h10"/></svg>
<h3 class="abs why-head" style="top:2477px">Lower Transaction Fees</h3>
<p class="abs why-text" style="top:2508px">We offer the lowest online processing fees (2.65%) in the wedding industry, meaning you keep more of your money.</p>

<!-- footer -->
<footer class="abs footer"></footer>
<h4 class="abs foot-head" style="left:86px;top:2621px">CONTACT US</h4>
<div class="abs field" style="top:2657px;height:37px">Name</div>
<div class="abs field" style="top:2702px;height:37px">Email</div>
<div class="abs field" style="top:2747px;height:66px">Message</div>
<a class="abs btn" style="left:86px;top:2826px;width:128px;height:34px;letter-spacing:1px">SEND</a>

<h4 class="abs foot-head" style="left:592px;top:2621px">QUICK LINKS</h4>
<a class="abs foot-link" style="top:2652px">Home</a>
<a class="abs foot-link" style="top:2673px">About Us</a>
<a class="abs foot-link" style="top:2694px">Wedding Professionals</a>
<a class="abs foot-link" style="top:2715px">Engaged Couples</a>
<h4 class="abs foot-head" style="left:592px;top:2762px">SOCIAL LINKS</h4>
<span class="abs social" style="left:592px"></span>
<span class="abs social" style="left:633px"></span>
<span class="abs social" style="left:674px"></span>

<div class="abs brand" style="left:927px;top:2638px;font-size:40px"><span class="brand-dot"></span>Marquiso</div>
<a class="abs btn" style="left:927px;top:2717px;width:187px;height:34px;letter-spacing:1px">ACCESS DEMO</a>
<p class="abs copy" style="top:2774px">Copyright © 2018<br>All Rights Reserved.</p>

</body>
</html>
```